Brookfarrow Osteopathy and dry needling business card

Business card for Brookfarrow Osteopathy and Dry Needling.

Industry/Entity Type

Health

Contact Information for Business Card

I do not have a phone number yet. I also do not have an email address yet. The physical address is: 48 Lower Crane Street Brookfarrow The website is: www.brookfarrowosteosteopathy.example My details are: Dr Martin Pellowe, Osteopath (B.Clin.Sci (Ost) M.Ost BSC ECON (Hons)

Colors
0094D4
00A9DD
6FCCEA
C7EBF8
E9F6FB

Requirements
Must have
• logo on the back
Nice to have
• Maybe a space for me to write an appointment time and date on the card.

```html
<!DOCTYPE html>
<html lang="en">
<head>
<meta charset="utf-8">
<title>Brookfarrow Osteopathy and Dry Needling – Business Card</title>
<link rel="stylesheet" href="https://fonts.googleapis.com/css2?family=Outfit:wght@400;500;700&display=swap">
<style>
  :root {
    --backdrop: #a6a6a6;
    --card-white: #ffffff;
    --accent-orange: #f58b2b;
    --brand-blue: #0094d4;
    --ink: #1c1c1c;
    --rule: #111111;
  }
  * { box-sizing: border-box; margin: 0; padding: 0; }
  html, body { width: 1200px; height: 1200px; overflow: hidden; }
  body {
    position: relative;
    background: var(--backdrop);
    font-family: "Outfit", sans-serif;
    color: var(--ink);
  }
  .card {
    position: absolute;
    left: 141px;
    width: 919px;
    height: 523px;
    overflow: hidden;
    box-shadow: 6px 10px 14px rgba(0, 0, 0, 0.35);
  }
  .card--front { top: 52px; background: var(--accent-orange); }
  .card--back  { top: 625px; background: var(--brand-blue); }

  .card__face {
    position: absolute;
    background: var(--card-white);
  }
  .card--front .card__face {
    left: 21px; top: 21px; right: 0; bottom: 0;
    border-top-left-radius: 92px;
  }
  .card--back .card__face {
    left: 0; top: 0; right: 22px; bottom: 19px;
    border-bottom-right-radius: 92px;
  }

  .holder-name {
    position: absolute;
    left: 44px; top: 230px;
    font-size: 38px;
    font-weight: 700;
    line-height: 1.2;
    color: var(--brand-blue);
    letter-spacing: 0.2px;
    white-space: nowrap;
  }
  .holder-credentials {
    position: absolute;
    left: 44px; top: 286px;
    font-size: 19px;
    font-weight: 400;
    white-space: nowrap;
  }
  .divider {
    position: absolute;
    left: 44px; top: 342px;
    width: 613px; height: 3px;
    background: var(--rule);
  }
  .contact-list {
    position: absolute;
    left: 44px; top: 377px;
    list-style: none;
  }
  .contact-list li {
    display: flex;
    align-items: center;
    gap: 18px;
    font-size: 22px;
    height: 37px;
    white-space: nowrap;
  }
  .contact-list svg { width: 20px; height: 20px; flex: none; }

  .brand-seal {
    position: absolute;
    display: flex;
    align-items: center;
    justify-content: center;
    text-align: center;
    border: 3px solid var(--brand-blue);
    border-radius: 50%;
    color: var(--brand-blue);
    font-weight: 500;
    line-height: 1.2;
    text-transform: uppercase;
  }
  .brand-seal--front {
    left: 631px; top: 51px;
    width: 194px; height: 194px;
    font-size: 16px;
    padding: 20px;
  }
  .brand-seal--back {
    left: 305px; top: 105px;
    width: 310px; height: 310px;
    font-size: 27px;
    padding: 34px;
  }
</style>
</head>
<body>
  <section class="card card--front" aria-label="Business card front">
    <div class="card__face">
      <div class="brand-seal brand-seal--front">Brookfarrow Osteopathy &amp; Dry Needling</div>
      <h1 class="holder-name">Dr Martin Pellowe</h1>
      <p class="holder-credentials">Osteopath (B.Clin.Sci (Ost) M.Ost BSC ECON (Hons)</p>
      <div class="divider"></div>
      <ul class="contact-list">
        <li>
          <svg viewBox="0 0 24 24" aria-hidden="true"><path d="M12 2a7 7 0 0 0-7 7c0 5 7 13 7 13s7-8 7-13a7 7 0 0 0-7-7zm0 9.5A2.5 2.5 0 1 1 12 6.5a2.5 2.5 0 0 1 0 5z" fill="#1c1c1c"/></svg>
          48 Lower Crane Street Brookfarrow
        </li>
        <li>
          <svg viewBox="0 0 24 24" aria-hidden="true"><circle cx="12" cy="12" r="10" fill="#1c1c1c"/><path d="M2 12h20M12 2c3 3 3 17 0 20M12 2c-3 3-3 17 0 20" stroke="#fff" stroke-width="1.6" fill="none"/></svg>
          www.brookfarrowosteosteopathy.example
        </li>
      </ul>
    </div>
  </section>

  <section class="card card--back" aria-label="Business card back">
    <div class="card__face">
      <div class="brand-seal brand-seal--back">Brookfarrow Osteopathy &amp; Dry Needling</div>
    </div>
  </section>
</body>
</html>
```